Stationery Design Project

Fire and building compliance company needs business card, letterhead and complement slip designed.
Have included a brief about business card, basic want front keep quite clean with just the MAS logo and the words Marbeck Alarm and Safety 2012 Ltd (small print) along the bottom. Website needs to be included (www.masalarm.example.nz) on either front or back.
The info for back is as per attachment.
Letterhead and complement slip should have the usual stuff MAS logo etc and also the accredited test lab logo at the bottom (can be small size)
Target Market(s)
Property owners, buisness managers
Industry/Entity Type
Building
Look and feel

```html
<!DOCTYPE html>
<html lang="en">
<head>
<meta charset="utf-8">
<title>MAS Stationery Set</title>
<link href="https://fonts.googleapis.com/css2?family=Montserrat:wght@400;500;600;700&display=swap" rel="stylesheet">
<style>
:root{
  --backdrop:#a7a9ac;
  --paper:#ffffff;
  --edge:#c9cbce;
  --ink:#3d3d3f;
  --teal:#0a5f86;
  --blue:#1aa3dc;
  --navy:#0b4b66;
  --orange:#f7a51c;
  --red:#e8432a;
  --flame:#f26a21;
}
*{margin:0;padding:0;box-sizing:border-box}
html,body{width:1200px;height:901px;overflow:hidden;background:#fff;font-family:"Montserrat",sans-serif}
.stage{position:absolute;left:50px;top:0;width:1105px;height:854px;background:var(--backdrop);overflow:hidden}
.piece{position:absolute;background:var(--paper);overflow:hidden;box-shadow:0 14px 18px -8px rgba(0,0,0,.35)}
.brand{position:absolute;display:flex;align-items:center;gap:6px}
.brand-dot{border-radius:50%;background:var(--flame);flex:none}
.brand-name{font-weight:600;color:var(--ink);line-height:1}
.brand-tag{color:var(--ink);font-weight:400;line-height:1.05}
.bar{position:absolute}
.bar-warm{background:linear-gradient(90deg,var(--orange),var(--red))}
.bar-cool{background:linear-gradient(90deg,var(--blue),var(--navy))}
.bar-warm-v{background:linear-gradient(180deg,var(--orange),var(--red))}
.bar-cool-v{background:linear-gradient(180deg,var(--blue),var(--navy))}
.web{position:absolute;font-weight:600;color:#222;letter-spacing:.08em}

/* business card front */
.card-front{left:62px;top:100px;width:445px;height:254px}
.card-front .brand{left:50px;top:66px;gap:14px}
.card-front .brand-dot{width:92px;height:92px}
.card-front .brand-name{font-size:58px}
.card-front .brand-tag{font-size:17px}
.card-front .legal{position:absolute;left:14px;top:230px;font-size:13px;letter-spacing:.34em;color:var(--ink)}

/* business card back */
.card-back{left:62px;top:460px;width:445px;height:254px}
.card-back .brand{left:12px;top:8px}
.card-back .brand-dot{width:44px;height:44px}
.card-back .brand-name{font-size:26px}
.card-back .brand-tag{font-size:8px}
.card-back .web{right:10px;top:12px;font-size:12px}
.worker{position:absolute;left:43px;top:90px}
.worker-name{font-size:19px;font-weight:700;color:var(--ink)}
.worker-co{font-size:12px;font-weight:600;color:var(--ink)}
.divider{position:absolute;left:236px;top:78px;width:2px;height:54px;background:var(--ink)}
.contact{position:absolute;left:246px;top:80px;font-size:10.5px;line-height:1.35;color:var(--ink)}
.contact b{font-weight:700}
.badge{position:absolute;left:8px;top:208px;width:22px;height:26px;background:var(--navy)}
.services{position:absolute;left:30px;right:10px;top:212px;text-align:center;font-size:7.6px;font-weight:600;color:var(--teal);line-height:1.45}

/* letterhead */
.letterhead{left:553px;top:80px;width:506px;height:655px}
.letterhead .brand,.slip .brand{left:14px;top:12px}
.letterhead .brand-dot,.slip .brand-dot{width:46px;height:46px}
.letterhead .brand-name,.slip .brand-name{font-size:24px}
.letterhead .brand-tag,.slip .brand-tag{font-size:7.5px}
.letterhead .web,.slip .web{right:10px;top:14px;font-size:10px;letter-spacing:.04em}
.footer{position:absolute;left:0;right:0;top:607px;text-align:center;color:var(--teal);font-size:8.5px;font-weight:600;line-height:1.3}
.footer .co,.slip-info .co{font-size:12px;font-weight:700}

/* compliments slip */
.slip{left:590px;top:347px;width:501px;height:246px;border:1px solid var(--edge);z-index:2;box-shadow:0 16px 20px -8px rgba(0,0,0,.4)}
.slip-info{position:absolute;right:10px;top:184px;text-align:right;color:var(--teal);font-size:8.5px;font-weight:600;line-height:1.4}
.with-comp{position:absolute;left:20px;top:220px;font-size:12px;font-weight:700;color:var(--teal)}
</style>
</head>
<body>
<div class="stage">

  <section class="piece card-front" aria-label="Business card front">
    <div class="brand">
      <span class="brand-dot"></span>
      <div><div class="brand-name">MAS</div><div class="brand-tag">Fire and Building<br>Compliance</div></div>
    </div>
    <div class="bar bar-cool-v" style="left:386px;top:0;width:16px;height:254px"></div>
    <div class="bar bar-warm-v" style="left:408px;top:0;width:16px;height:254px"></div>
    <p class="legal">Marbeck Alarm and Safety</p>
  </section>

  <section class="piece card-back" aria-label="Business card back">
    <div class="brand">
      <span class="brand-dot"></span>
      <div><div class="brand-name">MAS</div><div class="brand-tag">Fire and Building<br>Compliance</div></div>
    </div>
    <p class="web">www.masalarm.example.nz</p>
    <div class="bar bar-warm" style="left:159px;top:31px;width:286px;height:11px"></div>
    <div class="bar bar-cool" style="left:159px;top:49px;width:286px;height:11px"></div>
    <div class="worker">
      <p class="worker-name">WORKERS NAME</p>
      <p class="worker-co">Marbeck Alarm and Safety</p>
    </div>
    <div class="divider"></div>
    <p class="contact">14 Kowhai Lane Extension,<br>Whanganui, 4501<br><b>Phone</b> 06 555 0182,<br><b>fax</b> 06 555 0147<br><b>Email</b> admin@masalarm.example.nz</p>
    <div class="badge" aria-label="Accredited test lab badge"></div>
    <p class="services">Building compliance specialists &bull; Building warrant of fitness preparation<br>Fire alarms, Fire Extinguishers &amp; emergency lighting &bull; Approved evacuation schemes<br>Pressure testing LPG CNG Fire extinguishers &bull; Security alarm and CCTV systems</p>
  </section>

  <section class="piece letterhead" aria-label="Letterhead">
    <div class="brand">
      <span class="brand-dot"></span>
      <div><div class="brand-name">MAS</div><div class="brand-tag">Fire and Building<br>Compliance</div></div>
    </div>
    <p class="web">www.masalarm.example.nz</p>
    <div class="bar bar-warm" style="left:160px;top:32px;width:346px;height:12px"></div>
    <div class="bar bar-cool" style="left:160px;top:50px;width:346px;height:12px"></div>
    <div class="footer">
      <p class="co">Marbeck Alarm and Safety</p>
      <p>14 Kowhai Lane Extension, Whanganui, 4501</p>
      <p>Phone 06 555 0182, fax 06 555 0147 &nbsp;&bull;&nbsp; Email admin@masalarm.example.nz</p>
    </div>
  </section>

  <section class="piece slip" aria-label="Compliments slip">
    <div class="brand">
      <span class="brand-dot"></span>
      <div><div class="brand-name">MAS</div><div class="brand-tag">Fire and Building<br>Compliance</div></div>
    </div>
    <p class="web">www.masalarm.example.nz</p>
    <div class="bar bar-warm" style="left:160px;top:34px;right:0;height:11px"></div>
    <div class="bar bar-cool" style="left:160px;top:52px;right:0;height:10px"></div>
    <div class="slip-info">
      <p class="co">Marbeck Alarm and Safety</p>
      <p>14 Kowhai Lane Extension, Whanganui, 4501</p>
      <p>Phone 06 555 0182, fax 06 555 0147</p>
      <p>Email admin@masalarm.example.nz</p>
    </div>
    <p class="with-comp">With compliments</p>
  </section>

</div>
</body>
</html>
```